School Signage

I am wanting designs for signs completed that prompt students of the school requirements for hats, preparation and play.

I've uploaded rough examples of what we're after, but we would like them stylised and better than the example, including:
- A stylised logo/graphic for the 'Mervale 1, 2, 3'
- Clear, crisp signage for the words.
- Graphics that reinforce the message of the sign.

We're after three signs:
- One that will be located on the oval to prompt hat use.
- One that will be near the entry prompting the morning routine (please make this one landscape with instructions for 'on time' on one side, and 'late' on the other).
- One that will be located within the school prompting readiness for class.

```html
<!DOCTYPE html>
<html lang="en">
<head>
<meta charset="utf-8">
<title>Mervale hat sign</title>
<link href="https://fonts.googleapis.com/css2?family=Arimo:wght@400;700&display=swap" rel="stylesheet">
<style>
  :root {
    --mat: #d1d2d4;
    --paper: #ffffff;
    --forest: #1c3a1f;
    --ink: #163a1c;
    --tag-ink: #2a2a2a;
    --tag-edge: #4a2a2a;
    --sun: #ffe000;
    --white: #ffffff;
  }
  * { margin: 0; padding: 0; box-sizing: border-box; }
  html, body { width: 926px; height: 1200px; overflow: hidden; background: var(--mat); }
  body { position: relative; font-family: "Arimo", Arial, sans-serif; }

  .sign {
    position: absolute; left: 79px; top: 71px;
    width: 768px; height: 1053px;
    background: var(--paper); overflow: hidden;
  }
  .headline {
    position: absolute; left: 81px; top: 52px;
    font-weight: 700; font-size: 48px; line-height: 50px;
    color: var(--ink); letter-spacing: -0.3px;
  }
  .tag {
    position: absolute; left: 83px; top: 171px;
    width: 378px; height: 70px;
  }
  .tag::before {
    content: ""; position: absolute; left: 8px; top: 8px; right: -8px; bottom: -8px;
    background: var(--sun); border: 1.5px solid var(--tag-edge); border-radius: 10px;
  }
  .tag-label {
    position: absolute; inset: 0;
    background: var(--paper); border: 1.5px solid var(--tag-edge); border-radius: 10px;
    padding-left: 31px; display: flex; align-items: center;
    font-size: 33px; color: var(--tag-ink);
  }

  .steps { position: absolute; left: 0; top: 459px; width: 100%; }
  .step { position: absolute; width: 240px; text-align: center; }
  .step-walk { left: 33px; }
  .step-sit  { left: 267px; }
  .step-play { left: 501px; }
  .step-icon { display: block; width: 157px; height: 157px; margin: 0 auto; }
  .step-icon .ring { fill: none; stroke: var(--ink); stroke-width: 2; }
  .step-icon .limb { fill: none; stroke: var(--ink); stroke-linecap: round; stroke-linejoin: round; }
  .step-icon .solid { fill: var(--ink); }
  .step-label {
    margin-top: 24px;
    font-weight: 700; font-size: 34px; color: var(--ink);
  }
  .step-walk .step-label { margin-left: -48px; }
  .step-sit .step-label { margin-left: -22px; }
  .step-play .step-label { margin-left: 28px; }

  .footer-wave { position: absolute; left: 0; top: 790px; width: 768px; height: 263px; }
  .value {
    position: absolute; left: 391px; top: 912px;
    font-weight: 700; font-size: 40px; color: var(--white);
  }
  .school-mark {
    position: absolute; left: 560px; top: 918px;
    display: flex; align-items: center; gap: 10px;
    font-weight: 700; font-size: 17px; line-height: 20px; color: var(--white);
  }
  .school-dot { width: 26px; height: 26px; border-radius: 50%; background: var(--sun); flex: none; }
</style>
</head>
<body>
  <main class="sign">
    <h1 class="headline">We wear hats at<br>Mervale when outdoors...</h1>

    <div class="tag"><div class="tag-label">The Mervale 1, 2, 3</div></div>

    <section class="steps">
      <div class="step step-walk">
        <svg class="step-icon" viewBox="0 0 157 157" role="img" aria-label="Walking pictogram">
          <circle class="ring" cx="78.5" cy="78.5" r="77"/>
          <circle class="solid" cx="85" cy="36" r="8.5"/>
          <polyline class="limb" stroke-width="12" points="84,52 78.5,89"/>
          <polyline class="limb" stroke-width="8" points="64,60 58,78"/>
          <polyline class="limb" stroke-width="8" points="83,53 64,60"/>
          <polyline class="limb" stroke-width="8" points="84,54 93,68.5 108,78"/>
          <polyline class="limb" stroke-width="9" points="78.5,89 69,107 57,123"/>
          <polyline class="limb" stroke-width="9" points="79,89 89,102 98,124"/>
        </svg>
        <p class="step-label">1. Walking</p>
      </div>
      <div class="step step-sit">
        <svg class="step-icon" viewBox="0 0 157 157" role="img" aria-label="Sitting pictogram">
          <circle class="ring" cx="78.5" cy="78.5" r="77"/>
          <circle class="solid" cx="66" cy="29" r="12"/>
          <polyline class="limb" stroke-width="8" points="46,62 51,102 92,106"/>
          <polyline class="limb" stroke-width="13" points="64,52 67,86 103,89 112,133"/>
          <polyline class="limb" stroke-width="9" points="68,79 96,79"/>
        </svg>
        <p class="step-label">2. Sitting</p>
      </div>
      <div class="step step-play">
        <svg class="step-icon" viewBox="0 0 157 157" role="img" aria-label="Playing with a ball pictogram">
          <circle class="ring" cx="78.5" cy="78.5" r="77"/>
          <circle class="solid" cx="86.5" cy="47.5" r="8.5"/>
          <polyline class="limb" stroke-width="12" points="89,63 87,96"/>
          <polyline class="limb" stroke-width="8" points="86,65 54,73"/>
          <polyline class="limb" stroke-width="8" points="92,66 99,80 95,88"/>
          <polyline class="limb" stroke-width="9" points="86,96 68,110 62,127"/>
          <polyline class="limb" stroke-width="9" points="90,96 106,128"/>
          <circle class="solid" cx="45.5" cy="122" r="8.5"/>
        </svg>
        <p class="step-label">3. Playing</p>
      </div>
    </section>

    <svg class="footer-wave" viewBox="0 0 768 263" role="img" aria-label="Green base band with dotted flowing line pattern">
      <path d="M0 50 C 80 75, 150 75, 200 72 C 360 62, 560 10, 690 18 C 730 20, 755 25, 768 32 L768 263 L0 263 Z" fill="var(--forest)"/>
    </svg>

    <p class="value">Integrity</p>
    <div class="school-mark"><span class="school-dot"></span><span>Mervale<br>State High</span></div>
  </main>
</body>
</html>
```